Crestline Alloy Partners Business Card

Design a business card for a new company. Crestline Alloy Partners is a subsidiary of KVT, Inc. (www.kvtreclaims.example)

Target Market(s)

B2B, Manufactures

Industry/Entity Type

Recycling

Contact Information for Business Card

Crestline Alloy Partners, LLC.
40517 West Fennimore Lane
Dorwick IL 60594
P: (555) 309-4462
F: (555) 309-4461
www.crestap.example
Email@crestap.example

Font styles to use
Sans Serif

Requirements
Must have
• A KVT, Inc. subsidiary company.
Nice to have
• Recycling Solutions. Uncompromised. (slogan)

```html
<!DOCTYPE html>
<html lang="en">
<head>
<meta charset="utf-8">
<title>Crestline Alloy Partners Business Card</title>
<link rel="stylesheet" href="https://fonts.googleapis.com/css2?family=Questrial&family=Open+Sans:ital,wght@0,600;0,700;1,400&display=swap">
<style>
  :root {
    --page-bg: #a4a6a8;
    --steel-light: #f3f4f5;
    --steel-mid: #d9dbdd;
    --steel-dark: #c4c7ca;
    --navy: #1b2f86;
    --navy-deep: #132470;
    --royal: #2a5fb0;
    --green: #3f8a2a;
    --ink: #2a2a2a;
    --silver-text: #d3d6da;
    --slogan: #dfe6f3;
    --divider: #b9bcbf;
  }
  * { margin: 0; padding: 0; box-sizing: border-box; }
  html, body { width: 1105px; height: 1200px; overflow: hidden; }
  body {
    background: var(--page-bg);
    position: relative;
    font-family: "Questrial", sans-serif;
  }
  .card {
    position: absolute;
    left: 182px;
    width: 746px;
    height: 427px;
    overflow: hidden;
  }
  /* Front */
  .card-front {
    top: 119px;
    background:
      repeating-linear-gradient(0deg, rgba(255,255,255,0.25) 0 1px, rgba(0,0,0,0.03) 1px 3px),
      linear-gradient(100deg, var(--steel-mid) 0%, var(--steel-light) 45%, var(--steel-dark) 100%);
  }
  .brand-name {
    position: absolute;
    left: 80px;
    top: 170px;
    width: 290px;
    text-align: center;
    font-family: "Questrial", sans-serif;
    font-size: 30px;
    line-height: 1.15;
    color: var(--navy);
  }
  .divider {
    position: absolute;
    left: 397px;
    top: 225px;
    width: 1px;
    height: 115px;
    background: var(--divider);
  }
  .contact {
    position: absolute;
    left: 443px;
    top: 54px;
    color: var(--ink);
  }
  .person-name {
    font-family: "Open Sans", sans-serif;
    font-weight: 600;
    font-size: 28px;
    color: var(--navy);
    line-height: 1.2;
  }
  .person-title {
    font-size: 20px;
    color: var(--green);
    line-height: 1.3;
    margin-bottom: 14px;
  }
  .company {
    font-family: "Open Sans", sans-serif;
    font-weight: 700;
    font-size: 17px;
    line-height: 1.5;
  }
  .address { font-size: 18px; line-height: 1.45; margin-bottom: 12px; }
  .lines { list-style: none; }
  .lines li {
    display: flex;
    align-items: center;
    gap: 14px;
    font-size: 18px;
    line-height: 29px;
  }
  .lines svg { width: 18px; height: 18px; fill: var(--navy); flex: none; }
  .front-band {
    position: absolute;
    left: 0; bottom: 0;
    width: 100%;
    height: 35px;
    background: linear-gradient(90deg, var(--navy-deep), var(--royal) 40%, var(--navy-deep));
    border-top: 3px solid var(--green);
  }
  /* Back */
  .card-back {
    top: 637px;
    background: radial-gradient(ellipse at 50% 50%, var(--royal) 0%, var(--navy) 55%, var(--navy-deep) 100%);
    text-align: center;
  }
  .back-brand {
    position: absolute;
    left: 0; right: 0;
    top: 150px;
    font-family: "Questrial", sans-serif;
    font-size: 44px;
    color: var(--silver-text);
  }
  .slogan {
    position: absolute;
    left: 0; right: 0;
    top: 260px;
    font-family: "Open Sans", sans-serif;
    font-style: italic;
    font-size: 19px;
    color: var(--slogan);
  }
</style>
</head>
<body>
  <section class="card card-front">
    <div class="brand-name">Crestline Alloy Partners</div>
    <div class="divider"></div>
    <div class="contact">
      <div class="person-name">Daniel Reeve</div>
      <div class="person-title">CEO/Founder</div>
      <div class="company">Crestline Alloy Partners, LLC.</div>
      <div class="address">40517 West Fennimore Lane<br>Dorwick IL 60594</div>
      <ul class="lines">
        <li><svg viewBox="0 0 24 24" aria-hidden="true"><path d="M6.6 10.8a15.1 15.1 0 0 0 6.6 6.6l2.2-2.2a1 1 0 0 1 1-.25 11.4 11.4 0 0 0 3.6.57 1 1 0 0 1 1 1V20a1 1 0 0 1-1 1A17 17 0 0 1 3 4a1 1 0 0 1 1-1h3.5a1 1 0 0 1 1 1c0 1.25.2 2.45.57 3.57a1 1 0 0 1-.25 1z"/></svg>(555) 309-4462</li>
        <li><svg viewBox="0 0 24 24" aria-hidden="true"><path d="M6 2h10l2 2v5H6z M3 10h18a1 1 0 0 1 1 1v8a1 1 0 0 1-1 1H3a1 1 0 0 1-1-1v-8a1 1 0 0 1 1-1z M6 14h12v2H6z" fill-rule="evenodd"/></svg>(555) 309-4461</li>
        <li><svg viewBox="0 0 24 24" aria-hidden="true"><path d="M2 5h20v14H2z M3 6l9 7 9-7v2l-9 7-9-7z" fill-rule="evenodd"/></svg>name@crestap.example</li>
        <li><svg viewBox="0 0 24 24" aria-hidden="true"><path d="M12 2a10 10 0 1 0 0 20 10 10 0 0 0 0-20zm-1 3c-2 1-3 3-2 4s3 0 3 2-2 2-2 4 1 3 1 4a8 8 0 0 1-6-11zm3 .2a8 8 0 0 1 5 11.5c-1-1-1-3-3-3s-2-2-1-3-1-3-1-5.5z"/></svg>www.crestap.example</li>
      </ul>
    </div>
    <div class="front-band"></div>
  </section>

  <section class="card card-back">
    <div class="back-brand">Crestline Alloy Partners</div>
    <div class="slogan">Recycling Solutions | Uncompromised</div>
  </section>
</body>
</html>
```